High-end residential home builder needs a business card design

We need a new business card design for a small residential construction company based in Boise, Idaho. We specialize in building custom high-end homes and remodels, with a focus on great design and craftsmanship.

We would like to use our current logo, but open to new color suggestions.
Just looking for a clean, sharp, modern design that looks high-end.

Target Market(s)

Upscale clientele

Industry/Entity Type

Contractor

Contact Information for Business Card

Company: Stonefield Custom Builders
Name: Marcus Tilley
Phone number: 208 367 4120
Email: MarcusTilleySCB@mailbox-example.com
Website: Stonefieldcustombuilders-example.com

Font styles to use
Serif
Sans Serif

Requirements
Must have
• Company Logo
Company name
My name
My phone number
My email
Company website
Nice to have
• I have attached a few photos of cards that I really like.

```html
<!DOCTYPE html>
<html lang="en">
<head>
<meta charset="utf-8">
<title>Stonefield Custom Builders – Business Card</title>
<link rel="stylesheet" href="https://fonts.googleapis.com/css2?family=Montserrat:wght@500;700&family=Lato:wght@400&display=swap">
<style>
  :root {
    --brown: #331e0c;
    --orange: #e08e29;
    --white: #ffffff;
    --ink: #2a1a0c;
    --rule: #c9c9c9;
    --backdrop: #1f1f1f;
  }
  * { margin: 0; padding: 0; box-sizing: border-box; }
  html, body { width: 1200px; height: 1015px; overflow: hidden; }
  body { background: var(--backdrop); position: relative; font-family: "Lato", sans-serif; }

  .card {
    position: absolute;
    width: 600px;
    height: 343px;
    overflow: hidden;
    box-shadow: 0 14px 30px rgba(0,0,0,.55);
  }

  /* Front */
  .card--front { left: 90px; top: 100px; background: var(--orange); }
  .card--front .split { position: absolute; inset: 0; width: 100%; height: 100%; }
  .front-name {
    position: absolute; inset: 0;
    display: flex; align-items: center; justify-content: center; gap: 16px;
    font-family: "Montserrat", sans-serif; font-weight: 700;
    font-size: 30px; letter-spacing: 3px; text-transform: uppercase;
    color: var(--white); text-align: center; line-height: 1.2;
  }
  .front-name .mark { width: 22px; height: 22px; background: var(--white); flex: none; }

  /* Back */
  .card--back { left: 510px; top: 540px; background: var(--white); }
  .brand {
    position: absolute; left: 34px; top: 96px; width: 230px;
    display: flex; flex-direction: column; align-items: center; gap: 14px;
  }
  .brand .mark { width: 42px; height: 42px; border: 3px solid var(--brown); }
  .brand-name {
    font-family: "Montserrat", sans-serif; font-weight: 700; color: var(--brown);
    font-size: 17px; letter-spacing: 4px; text-transform: uppercase; text-align: center; line-height: 1.5;
  }
  .divider { position: absolute; left: 290px; top: 70px; width: 1px; height: 150px; background: var(--rule); }
  .contact { position: absolute; left: 312px; top: 78px; }
  .contact-name {
    font-family: "Montserrat", sans-serif; font-weight: 700; color: var(--ink);
    font-size: 19px; letter-spacing: .5px; text-transform: uppercase; margin-bottom: 12px;
  }
  .contact-list { list-style: none; font-size: 12.5px; color: var(--ink); }
  .contact-list li { display: flex; align-items: center; gap: 9px; height: 22px; }
  .contact-list svg { width: 13px; height: 13px; flex: none; fill: var(--ink); }
  .accent { color: var(--orange); }

  .strip-orange { position: absolute; left: 0; bottom: 0; width: 360px; height: 14px; background: var(--orange); }
  .tagline-band {
    position: absolute; right: 0; bottom: 0; width: 270px; height: 58px; background: var(--brown);
    display: flex; align-items: center; justify-content: center;
    font-family: "Montserrat", sans-serif; font-weight: 500; font-size: 15px; letter-spacing: 1px;
    color: var(--orange); text-transform: uppercase; white-space: nowrap;
  }
</style>
</head>
<body>

<section class="card card--front">
  <svg class="split" viewBox="0 0 600 343" preserveAspectRatio="none" aria-hidden="true">
    <polygon points="0,0 240,0 430,343 0,343" fill="var(--brown)"/>
  </svg>
  <div class="front-name"><span class="mark"></span>Stonefield<br>Custom Builders</div>
</section>

<section class="card card--back">
  <div class="brand">
    <span class="mark"></span>
    <p class="brand-name">Stonefield<br>Custom Builders</p>
  </div>

  <div class="divider"></div>

  <div class="contact">
    <h1 class="contact-name">Marcus Tilley</h1>
    <ul class="contact-list">
      <li>
        <svg viewBox="0 0 24 24"><path d="M6.6 10.8a15 15 0 0 0 6.6 6.6l2.2-2.2a1 1 0 0 1 1-.25 11.4 11.4 0 0 0 3.6.57 1 1 0 0 1 1 1V20a1 1 0 0 1-1 1A17 17 0 0 1 3 4a1 1 0 0 1 1-1h3.5a1 1 0 0 1 1 1c0 1.25.2 2.46.57 3.6a1 1 0 0 1-.25 1z"/></svg>
        208 367 4120
      </li>
      <li>
        <svg viewBox="0 0 24 24"><path d="M2 5h20v14H2z M2 5l10 8 10-8" fill="none" stroke="currentColor" stroke-width="2"/></svg>
        MarcusTilleySCB@mailbox-example.com
      </li>
      <li>
        <svg viewBox="0 0 24 24"><circle cx="12" cy="12" r="10" fill="none" stroke="currentColor" stroke-width="2"/><path d="M2 12h20M12 2c3 3 3 17 0 20M12 2c-3 3-3 17 0 20" fill="none" stroke="currentColor" stroke-width="1.6"/></svg>
        <span>www.<span class="accent">Stonefieldcustombuilders-example</span>.com</span>
      </li>
    </ul>
  </div>

  <div class="strip-orange"></div>
  <div class="tagline-band">Crafted With Precision</div>
</section>

</body>
</html>
```